Biz Cards, Letterhead
Pls Use Imagination and Refer to Logo Attached. Completely open to ideas. You're the creative ones!
Biz Cards, Letterhead - Consulting
Creative Brief
Simple
Corinne M Dashelt
President & CEO
28516 Belvorne Court Lewes, DE 19958
CDashelt@TheDasheltGroup.example
Don't have to have the text on the back of the card but it is a possibility. Overall, the idea is to be cutting edge, innovative, professional, yet simple. Thanks!
Supply Chain Solutions....Providing Innovation, Automation, & Optimization.

```html
<!DOCTYPE html>
<html lang="en">
<head>
<meta charset="utf-8">
<title>The Dashelt Group — Stationery</title>
<link rel="stylesheet" href="https://fonts.googleapis.com/css2?family=Cormorant+Garamond:wght@500&family=Open+Sans:wght@400;600&display=swap">
<style>
:root{
  --board:#1d1d1f;
  --paper:#ffffff;
  --brand-blue:#3a55a4;
  --brand-gray:#7b7c80;
  --ink:#4a4a52;
  --faint:#e9ebf2;
}
*{margin:0;padding:0;box-sizing:border-box}
html,body{width:1200px;height:432px;overflow:hidden;background:var(--board);font-family:"Open Sans",Arial,sans-serif;color:var(--ink)}
.board{position:relative;width:1200px;height:432px}
.piece{position:absolute;background:var(--paper);overflow:hidden;box-shadow:0 2px 6px rgba(0,0,0,.5)}
.wordmark{font-family:"Cormorant Garamond",Georgia,serif;font-weight:500;color:var(--brand-blue);letter-spacing:.12em;text-transform:uppercase;white-space:nowrap;display:flex;align-items:center;gap:3px}
.wordmark .dot{width:5px;height:5px;border-radius:50%;background:currentColor;flex:none}
.faint-mark{position:absolute;font-family:"Cormorant Garamond",Georgia,serif;font-weight:500;color:var(--faint);text-transform:uppercase;letter-spacing:.1em;white-space:nowrap}
.fine{font-size:4px;line-height:6px;white-space:nowrap}
.footer-band{position:absolute;left:0;bottom:0;width:100%;height:16px}

/* business cards */
.card{left:17px;width:108px;height:80px}
.card--front-a{top:79px}
.card--front-b{top:167px}
.card--back-blue{top:255px;background:var(--brand-blue)}
.card--back-gray{top:343px;background:var(--brand-gray)}
.card .wordmark{position:absolute;top:8px;left:8px;font-size:6px}
.card .contact{position:absolute;left:8px;top:28px}
.card .contact .name{font-weight:600;font-size:4.5px}
.card .faint-mark{right:-4px;top:22px;font-size:22px;transform:rotate(-90deg);transform-origin:right top}
.card-back .wordmark{position:absolute;left:8px;top:14px;font-size:7px;color:var(--paper)}
.card-back .tagline{position:absolute;left:8px;bottom:12px;color:var(--paper);font-size:4px;line-height:6px}

/* letterhead */
.letterhead{top:36px;width:192px;height:384px}
.letterhead--one{left:137px}
.letterhead--two{left:341px}
.letterhead .wordmark{position:absolute;top:30px;left:22px;font-size:7px}
.letterhead .faint-mark{left:14px;top:70px;font-size:30px;transform:rotate(-90deg) translateX(-100%);transform-origin:left top}
.letterhead .fine{position:absolute;left:22px;bottom:20px}

/* envelopes */
.envelope{left:542px;width:188px}
.env-a{top:43px;height:88px}
.env-b{top:144px;height:64px;background:var(--brand-blue)}
.env-c{top:216px;height:90px;background:var(--brand-blue)}
.env-d{top:316px;height:104px}
.envelope svg{position:absolute;inset:0}
.envelope .wordmark{position:absolute;font-size:7px}

/* small envelopes */
.mini{left:941px;width:235px}
.mini-a{top:132px;height:84px}
.mini-b{top:223px;height:89px}
.mini-a .wordmark{position:absolute;left:14px;top:14px;font-size:7px}
.mini-b .band{position:absolute;left:0;right:0;top:0;height:62px;background:var(--brand-blue)}
.mini-b .wordmark{position:absolute;left:50%;bottom:6px;transform:translateX(-50%);font-size:7px}
</style>
</head>
<body>
<main class="board">

  <!-- business cards -->
  <section class="piece card card--front-a">
    <div class="wordmark"><span class="dot"></span>The Dashelt Group</div>
    <div class="faint-mark">Dashelt</div>
    <div class="contact fine">
      <p class="name">Corinne M Dashelt</p>
      <p>President &amp; CEO</p>
      <p>T 302.555.0147</p>
      <p>C 302.555.0192</p>
      <p>CDashelt@TheDasheltGroup.example</p>
      <p>TheDasheltGroup.example</p>
    </div>
    <svg class="footer-band" viewBox="0 0 108 16" preserveAspectRatio="none"><rect y="14" width="108" height="2" fill="#3a55a4"/><polygon points="80,16 108,6 108,16" fill="#7b7c80"/></svg>
  </section>
  <section class="piece card card--front-b">
    <div class="wordmark"><span class="dot"></span>The Dashelt Group</div>
    <div class="faint-mark">Dashelt</div>
    <div class="contact fine">
      <p class="name">Corinne M Dashelt</p>
      <p>President &amp; CEO</p>
      <p>T 302.555.0147</p>
      <p>C 302.555.0192</p>
      <p>CDashelt@TheDasheltGroup.example</p>
      <p>TheDasheltGroup.example</p>
    </div>
    <svg class="footer-band" viewBox="0 0 108 16" preserveAspectRatio="none"><rect y="14" width="108" height="2" fill="#3a55a4"/><polygon points="80,16 108,6 108,16" fill="#7b7c80"/></svg>
  </section>
  <section class="piece card card-back card--back-blue">
    <div class="wordmark">The Dashelt Group</div>
    <p class="tagline">Supply Chain Solutions<br>Providing Innovation, Automation, &amp; Optimization</p>
  </section>
  <section class="piece card card-back card--back-gray">
    <div class="wordmark">The Dashelt Group</div>
    <p class="tagline">Supply Chain Solutions<br>Providing Innovation, Automation, &amp; Optimization</p>
  </section>

  <!-- letterhead -->
  <section class="piece letterhead letterhead--one">
    <div class="faint-mark">Dashelt</div>
    <div class="wordmark"><span class="dot"></span>The Dashelt Group</div>
    <p class="fine">28516 Belvorne Court Lewes, DE 19958 &nbsp;|&nbsp; T 302.555.0147 &nbsp;|&nbsp; TheDasheltGroup.example</p>
    <svg class="footer-band" viewBox="0 0 192 16" preserveAspectRatio="none"><rect y="12" width="192" height="4" fill="#3a55a4"/><polygon points="150,16 192,2 192,16" fill="#7b7c80"/></svg>
  </section>
  <section class="piece letterhead letterhead--two">
    <div class="faint-mark">Dashelt</div>
    <div class="wordmark"><span class="dot"></span>The Dashelt Group</div>
    <p class="fine">28516 Belvorne Court Lewes, DE 19958 &nbsp;|&nbsp; T 302.555.0147 &nbsp;|&nbsp; TheDasheltGroup.example</p>
    <svg class="footer-band" viewBox="0 0 192 16" preserveAspectRatio="none"><rect y="12" width="192" height="4" fill="#3a55a4"/><polygon points="150,16 192,2 192,16" fill="#7b7c80"/></svg>
  </section>

  <!-- envelopes -->
  <section class="piece envelope env-a">
    <svg viewBox="0 0 188 88" preserveAspectRatio="none"><polygon points="0,34 94,62 188,34 188,88 0,88" fill="#3a55a4"/><polyline points="0,34 94,62 188,34" fill="none" stroke="#fff" stroke-width="1"/></svg>
    <div class="wordmark" style="left:14px;top:8px;font-size:6px"><span class="dot"></span>The Dashelt Group</div>
  </section>
  <section class="piece envelope env-b">
    <svg viewBox="0 0 188 64" preserveAspectRatio="none"><polygon points="0,0 94,24 188,0" fill="#fff"/></svg>
    <div class="wordmark" style="left:50%;top:36px;transform:translateX(-50%);color:#fff">The Dashelt Group</div>
  </section>
  <section class="piece envelope env-c">
    <svg viewBox="0 0 188 90" preserveAspectRatio="none"><polygon points="0,0 188,0 188,22 94,44 0,22" fill="#fff"/></svg>
    <div class="wordmark" style="left:50%;top:58px;transform:translateX(-50%);color:#fff">The Dashelt Group</div>
  </section>
  <section class="piece envelope env-d">
    <svg viewBox="0 0 188 104" preserveAspectRatio="none"><polyline points="0,30 94,60 188,30" fill="none" stroke="#d7d9e2" stroke-width="1"/><rect y="100" width="188" height="4" fill="#3a55a4"/><polygon points="150,104 188,92 188,104" fill="#7b7c80"/></svg>
    <div class="wordmark" style="left:50%;top:70px;transform:translateX(-50%)">The Dashelt Group</div>
  </section>

  <!-- small envelopes -->
  <section class="piece mini mini-a">
    <div class="wordmark"><span class="dot"></span>The Dashelt Group</div>
    <svg class="footer-band" viewBox="0 0 235 16" preserveAspectRatio="none"><rect y="13" width="235" height="3" fill="#3a55a4"/><polygon points="190,16 235,4 235,16" fill="#7b7c80"/></svg>
  </section>
  <section class="piece mini mini-b">
    <div class="band"></div>
    <div class="wordmark">The Dashelt Group</div>
  </section>

</main>
</body>
</html>
```